"WEB 3.0 BLOCKCHAIN" company website design

Need a dynamic website for WEB 3.0 BLOCKCHAIN company. The company offers CRYPTO TOKENS, NFT TOKENS, and CRYPTO WALLETS. The company focuses on ESG, GRC, NFT, DeFi, Decentralized Identity, DeWiFi, DeCloud technologies.

The primary colors of the company logo is "#33768B", "#00788C" and also uses White for dark background.

The website should include some animations for its technologies. The site design must show the newer WEB3.0 themes.

Target Market(s)

BLOCKCHAIN users

Industry/Entity Type

BLOCKCHAIN

Coding

Coded - Design and coding required

Number of Pages Required

1 page

Requirements
Must have
• WEB 3.0 THEMES

```html
<!DOCTYPE html>
<html lang="en">
<head>
<meta charset="utf-8">
<title>Nodechain – Web 3.0 Blockchain</title>
<link href="https://fonts.googleapis.com/css2?family=Exo+2:wght@400;700;800;900&family=Roboto:wght@400;500;700&display=swap" rel="stylesheet">
<style>
:root{
  --bg:#031417;
  --bg-deep:#020f11;
  --footer:#061a1d;
  --teal:#1a6f84;
  --teal-soft:#33768b;
  --teal-accent:#00788c;
  --white:#ffffff;
  --muted:#cfd8da;
  --ghost:rgba(255,255,255,0.045);
}
*{margin:0;padding:0;box-sizing:border-box}
html,body{width:1200px;height:4237px;overflow:hidden;background:var(--bg);color:var(--white);font-family:"Roboto",Arial,sans-serif}
.page{position:relative;width:1200px;height:4237px;overflow:hidden;background:var(--bg)}
.abs{position:absolute}
.display{font-family:"Exo 2","Roboto",sans-serif}

/* header */
.brand{position:absolute;display:flex;align-items:center;gap:12px;font-family:"Exo 2",sans-serif;font-weight:800;font-size:19px;letter-spacing:.5px}
.brand-dot{width:26px;height:26px;border-radius:50%;border:3px solid var(--teal-soft)}
.nav{position:absolute;left:447px;top:46px;display:flex;gap:28px;font-size:14px;font-weight:500}
.login{position:absolute;left:985px;top:38px;width:102px;height:36px;border-radius:18px;background:var(--teal);display:flex;align-items:center;justify-content:center;gap:7px;font-size:14px;font-weight:500}

/* side nav */
.step{position:absolute;left:28px;font-family:"Exo 2",sans-serif;font-weight:800;font-size:40px;line-height:1}
.dots{position:absolute;left:40px;display:flex;flex-direction:column;gap:16px}
.dots span{display:flex;align-items:center;gap:10px;height:10px;font-size:9px;color:var(--muted)}
.dots i{width:10px;height:10px;border-radius:50%;background:var(--white)}
.dots .on i{background:var(--teal-accent)}

/* hero */
.hero-title{left:135px;top:262px;font-size:54px;font-weight:800;letter-spacing:1px}
.hero-text{left:137px;top:344px;width:420px;font-size:16.5px;line-height:28px;font-weight:500}
.btn{position:absolute;display:flex;align-items:center;justify-content:center;gap:9px;border-radius:26px;background:var(--teal);font-size:15px;font-weight:700;letter-spacing:.3px}
.btn svg{width:15px;height:15px}
.globe{left:587px;top:117px;width:520px;height:520px;border-radius:50%;background:radial-gradient(circle at 50% 45%,rgba(31,125,145,.55),rgba(15,70,85,.35) 55%,rgba(3,20,23,0) 72%)}
.coin{position:absolute;border-radius:50%;background:radial-gradient(circle at 40% 35%,#e7c16e,#a9792d 60%,#5b3f16)}

/* section titles */
.ghost{position:absolute;left:0;width:1200px;text-align:center;font-family:"Exo 2",sans-serif;font-weight:900;font-size:120px;color:var(--ghost);letter-spacing:4px;line-height:1}
.sec-title{position:absolute;left:0;width:1200px;text-align:center;font-family:"Exo 2",sans-serif;font-weight:800;font-size:44px;line-height:1;letter-spacing:.5px}
.sec-title span{font-weight:400}
.sec-sub{position:absolute;left:0;width:1200px;text-align:center;font-size:14px}

.about-text{position:absolute;left:156px;top:826px;width:888px;text-align:center;font-size:13.5px;line-height:27px}
.about-text p+p{margin-top:12px}

.photo{position:absolute}

/* offer cards */
.card{position:absolute;top:1738px;width:304px;height:342px;overflow:hidden}
.card-label{position:absolute;left:0;right:0;bottom:34px;text-align:center;font-weight:700;font-size:20px}
.card-feature{background:linear-gradient(180deg,#0f5a6b,#1a6f84);display:flex;flex-direction:column;align-items:center;justify-content:center;text-align:center;padding:0 34px}
.card-feature h3{font-size:21px;font-weight:700;margin-top:40px}
.card-feature p{font-size:14px;line-height:24px;margin-top:10px}
.btn-light{position:static;margin-top:20px;width:154px;height:40px;background:var(--white);color:var(--teal);font-size:13.5px}

.wave{position:absolute;left:0;width:1200px;background:linear-gradient(180deg,rgba(3,20,23,0),rgba(17,72,82,.35) 50%,rgba(3,20,23,0))}

/* focus */
.focus{position:absolute;width:480px;height:110px}
.focus-icon{position:absolute;left:0;top:0;width:86px;height:86px}
.focus h4{position:absolute;left:123px;top:-4px;font-size:18px;font-weight:700}
.focus p{position:absolute;left:123px;top:34px;width:350px;font-size:14px;line-height:23px}

/* news */
.news{position:absolute;top:3511px;width:309px;height:426px;background:var(--bg-deep)}
.news-img{height:211px}
.date{position:absolute;left:20px;top:195px;height:30px;padding:0 14px;background:var(--teal);display:flex;align-items:center;gap:7px;font-size:13px}
.news h5{position:absolute;left:22px;top:250px;width:270px;font-size:16.5px;line-height:24px;font-weight:700}
.news p{position:absolute;left:22px;top:312px;width:270px;font-size:14px;line-height:22px}
.more{position:absolute;left:22px;top:370px;display:flex;align-items:center;gap:7px;color:var(--teal-soft);font-size:14px;font-weight:700}

/* footer */
.footer{position:absolute;left:0;top:4031px;width:1200px;height:206px;background:var(--footer)}
.footer-links{position:absolute;left:0;top:120px;width:1200px;display:flex;justify-content:center;gap:30px;font-size:14px}
.footer-links b{font-weight:400}
.copy{position:absolute;left:0;top:153px;width:1200px;text-align:center;font-size:13px}
</style>
</head>
<body>
<div class="page">

  <!-- header -->
  <div class="brand" style="left:112px;top:41px"><span class="brand-dot"></span>NODECHAIN</div>
  <nav class="nav"><span>Home</span><span>About Us</span><span>We Offer</span><span>Our Focus</span><span>News</span><span>Contact Us</span></nav>
  <div class="login">
    <svg width="12" height="13" viewBox="0 0 12 13"><rect x="1" y="5.5" width="10" height="7" rx="1" fill="#fff"/><path d="M3 5.5V4a3 3 0 0 1 6 0v1.5" stroke="#fff" stroke-width="1.6" fill="none"/></svg>Login
  </div>

  <!-- hero -->
  <div class="abs globe" role="img" aria-label="Glowing teal network globe made of connected dots"></div>
  <div class="step" style="top:286px">01</div>
  <div class="dots" style="top:348px"><span class="on"><i></i>Landing</span><span><i></i></span><span><i></i></span><span><i></i></span><span><i></i></span></div>
  <h1 class="abs display hero-title">BLOCKCHAIN</h1>
  <p class="abs hero-text">Lorem ipsum dolor sit amet, consectetur adipiscing sed do eiusmod tempor incididunt aliqua.</p>
  <div class="btn" style="left:138px;top:428px;width:193px;height:50px">GET STARTED
    <svg viewBox="0 0 16 16"><circle cx="8" cy="8" r="8" fill="#fff"/><path d="M6.5 4.5 10 8l-3.5 3.5" stroke="#1a6f84" stroke-width="2" fill="none"/></svg></div>

  <div class="coin" style="left:1082px;top:666px;width:118px;height:116px" role="img" aria-label="Gold crypto coin"></div>

  <!-- about -->
  <div class="ghost" style="top:700px">ABOUT US</div>
  <h2 class="sec-title" style="top:757px">DISCOVER <span>OUR STORY</span></h2>
  <div class="about-text">
    <p>Sed ut perspiciatis unde omnis iste natus error sit voluptatem accusantium doloremque laudantium, totam rem aperiam, eaque ipsa quae ab illo inventore veritatis et quasi architecto beatae vitae dicta sunt explicabo. Nemo enim ipsam voluptatem quia voluptas sit aspernatur aut odit aut fugit, sed quia consequuntur magni dolores eos qui ratione voluptatem sequi nesciunt.</p>
    <p>Neque porro quisquam est, qui dolorem ipsum quia dolor sit amet, consectetur, adipisci velit, sed quia non numquam eius modi tempora incidunt ut labore et dolore magnam aliquam quaerat voluptatem.</p>
  </div>
  <div class="btn" style="left:505px;top:1004px;width:190px;height:48px;font-size:14px">LEARN MORE
    <svg viewBox="0 0 16 16"><circle cx="8" cy="8" r="8" fill="#fff"/><path d="M6.5 4.5 10 8l-3.5 3.5" stroke="#1a6f84" stroke-width="2" fill="none"/></svg></div>
  <div class="step" style="top:1030px">02</div>
  <div class="dots" style="top:1092px"><span><i></i></span><span class="on"><i></i>About</span><span><i></i></span><span><i></i></span><span><i></i></span></div>
  <div class="photo" style="left:151px;top:1101px;width:898px;height:408px;background:radial-gradient(circle at 47% 55%,#b07a3a 0,#3b4a5c 22%,#12304a 55%,#0a1c2e 100%)" role="img" aria-label="Hand holding a glowing blockchain network of connected icons"></div>

  <div class="coin" style="left:-2px;top:1496px;width:117px;height:123px" role="img" aria-label="Gold crypto coin"></div>

  <!-- we offer -->
  <div class="ghost" style="top:1588px">SOLUTIONS</div>
  <h2 class="sec-title" style="top:1623px">WE OFFER</h2>
  <p class="sec-sub" style="top:1669px">Lorem ipsum dolor sit amet, consectetur adipiscing elit, sed do</p>
  <div class="step" style="top:1820px">03</div>
  <div class="dots" style="top:1882px"><span><i></i></span><span><i></i></span><span class="on"><i></i>Solution</span><span><i></i></span><span><i></i></span></div>

  <div class="card" style="left:112px;background:linear-gradient(180deg,#5c7f92,#243a4f 60%,#3a3326)" role="img" aria-label="Hand holding a phone over a night city with coin icons">
    <div class="card-label">CRYPTO TOKENS</div></div>
  <div class="card card-feature" style="left:447px">
    <h3>NFT TOKENS</h3>
    <p>Lorem ipsum dolor sit consectetur adipiscing elit, sed do eiusmod tempor incididunt enim labore aliqua.</p>
    <div class="btn btn-light">LEARN MORE
      <svg viewBox="0 0 16 16"><circle cx="8" cy="8" r="8" fill="#1a6f84"/><path d="M6.5 4.5 10 8l-3.5 3.5" stroke="#fff" stroke-width="2" fill="none"/></svg></div>
  </div>
  <div class="card" style="left:781px;background:linear-gradient(180deg,#1c5f82,#163e5a 55%,#3a3a22)" role="img" aria-label="Currency symbols floating over a city skyline">
    <div class="card-label">CRYPTO WALLETS</div></div>

  <div class="wave" style="top:2110px;height:290px"></div>
  <div class="abs" style="left:638px;top:2137px;width:123px;height:222px;border-radius:40% 40% 20% 20%;background:linear-gradient(180deg,#d99a2a,#b86d14)" role="img" aria-label="Cartoon mascot holding a gold coin"></div>

  <!-- focus -->
  <div class="ghost" style="top:2425px">FOCUSES</div>
  <h2 class="sec-title" style="top:2462px">OUR FOCUS</h2>
  <p class="sec-sub" style="top:2508px">Lorem ipsum dolor sit amet, consectetur adipiscing elit, sed do</p>
  <div class="step" style="top:2678px">04</div>
  <div class="dots" style="top:2740px"><span><i></i></span><span><i></i></span><span><i></i></span><span class="on"><i></i>Focus</span><span><i></i></span></div>

  <div class="focus" style="left:115px;top:2575px"><svg class="focus-icon" viewBox="0 0 86 86"><circle cx="43" cy="43" r="38" fill="none" stroke="#1a6f84" stroke-width="6"/></svg><h4>ESG</h4><p>Lorem ipsum dolor sit amet, consectetur adipiscing elit, sed do eiusmod tempor incididunt</p></div>
  <div class="focus" style="left:633px;top:2575px"><svg class="focus-icon" viewBox="0 0 86 86"><circle cx="43" cy="43" r="38" fill="none" stroke="#1a6f84" stroke-width="6"/></svg><h4>GRC</h4><p>Lorem ipsum dolor sit amet, consectetur adipiscing elit, sed do eiusmod tempor incididunt</p></div>
  <div class="focus" style="left:115px;top:2720px"><svg class="focus-icon" viewBox="0 0 86 86"><circle cx="43" cy="43" r="38" fill="none" stroke="#1a6f84" stroke-width="6"/></svg><h4>NFT</h4><p>Lorem ipsum dolor sit amet, consectetur adipiscing elit, sed do eiusmod tempor incididunt</p></div>
  <div class="focus" style="left:633px;top:2720px"><svg class="focus-icon" viewBox="0 0 86 86"><circle cx="43" cy="43" r="38" fill="none" stroke="#1a6f84" stroke-width="6"/></svg><h4>DeFi</h4><p>Lorem ipsum dolor sit amet, consectetur adipiscing elit, sed do eiusmod tempor incididunt</p></div>
  <div class="focus" style="left:115px;top:2865px"><svg class="focus-icon" viewBox="0 0 86 86"><circle cx="43" cy="43" r="38" fill="none" stroke="#1a6f84" stroke-width="6"/></svg><h4>Decentralized Identity</h4><p>Lorem ipsum dolor sit amet, consectetur adipiscing elit, sed do eiusmod tempor incididunt</p></div>
  <div class="focus" style="left:633px;top:2865px"><svg class="focus-icon" viewBox="0 0 86 86"><circle cx="43" cy="43" r="38" fill="none" stroke="#1a6f84" stroke-width="6"/></svg><h4>DeWiFi</h4><p>Lorem ipsum dolor sit amet, consectetur adipiscing elit, sed do eiusmod tempor incididunt</p></div>

  <div class="wave" style="top:3040px;height:280px"></div>
  <div class="abs" style="left:320px;top:3156px;width:198px;height:132px;border-radius:20px;background:linear-gradient(90deg,#c9801c,#e8b23a)" role="img" aria-label="Cartoon mascot leaning on a stack of gold coins"></div>

  <!-- news -->
  <div class="ghost" style="top:3356px">NEWS</div>
  <h2 class="sec-title" style="top:3395px">LATEST NEWS</h2>
  <p class="sec-sub" style="top:3443px">Lorem ipsum dolor sit amet, consectetur adipiscing elit, sed do</p>
  <div class="step" style="top:3628px">05</div>
  <div class="dots" style="top:3690px"><span><i></i></span><span><i></i></span><span><i></i></span><span><i></i></span><span class="on"><i></i>News</span></div>

  <article class="news" style="left:112px">
    <div class="news-img" style="background:radial-gradient(circle at 55% 40%,#a07436,#3a3a3a 50%,#15161a)" role="img" aria-label="Person using a phone with digital coin graphics"></div>
    <div class="date"><svg width="12" height="12" viewBox="0 0 12 12"><rect x="1" y="2" width="10" height="9" rx="1" fill="none" stroke="#fff" stroke-width="1.4"/><path d="M1 5h10" stroke="#fff" stroke-width="1.4"/></svg>Jan 2, 2022</div>
    <h5>Lorem ipsum amet, consectetur adipiscing elit</h5>
    <p>Sed ut perspiciatis unde omnis iste natus sit voluptatem accusantium</p>
    <div class="more">READ MORE <svg width="14" height="14" viewBox="0 0 16 16"><circle cx="8" cy="8" r="8" fill="#33768b"/><path d="M6.5 4.5 10 8l-3.5 3.5" stroke="#020f11" stroke-width="2" fill="none"/></svg></div>
  </article>
  <article class="news" style="left:444px">
    <div class="news-img" style="background:radial-gradient(circle at 50% 45%,#2d6fc2,#17306e 50%,#0a1430)" role="img" aria-label="Glowing blue blockchain data blocks"></div>
    <div class="date"><svg width="12" height="12" viewBox="0 0 12 12"><rect x="1" y="2" width="10" height="9" rx="1" fill="none" stroke="#fff" stroke-width="1.4"/><path d="M1 5h10" stroke="#fff" stroke-width="1.4"/></svg>Jan 2, 2022</div>
    <h5>Lorem ipsum amet, consectetur adipiscing elit</h5>
    <p>Sed ut perspiciatis unde omnis iste natus sit voluptatem accusantium</p>
    <div class="more">READ MORE <svg width="14" height="14" viewBox="0 0 16 16"><circle cx="8" cy="8" r="8" fill="#33768b"/><path d="M6.5 4.5 10 8l-3.5 3.5" stroke="#020f11" stroke-width="2" fill="none"/></svg></div>
  </article>
  <article class="news" style="left:776px">
    <div class="news-img" style="background:radial-gradient(circle at 50% 40%,#4a8da0,#23404c 55%,#11191d)" role="img" aria-label="Hands on a laptop with holographic data"></div>
    <div class="date"><svg width="12" height="12" viewBox="0 0 12 12"><rect x="1" y="2" width="10" height="9" rx="1" fill="none" stroke="#fff" stroke-width="1.4"/><path d="M1 5h10" stroke="#fff" stroke-width="1.4"/></svg>Jan 2, 2022</div>
    <h5>Lorem ipsum amet, consectetur adipiscing elit</h5>
    <p>Sed ut perspiciatis unde omnis iste natus sit voluptatem accusantium</p>
    <div class="more">READ MORE <svg width="14" height="14" viewBox="0 0 16 16"><circle cx="8" cy="8" r="8" fill="#33768b"/><path d="M6.5 4.5 10 8l-3.5 3.5" stroke="#020f11" stroke-width="2" fill="none"/></svg></div>
  </article>

  <!-- footer -->
  <footer class="footer">
    <div class="brand" style="left:512px;top:54px"><span class="brand-dot"></span>NODECHAIN</div>
    <div class="footer-links"><span>Home</span><b>|</b><span>About Us</span><b>|</b><span>We Offer</span><b>|</b><span>Our Focus</span><b>|</b><span>News</span><b>|</b><span>Contact Us</span></div>
    <div class="copy">© 2022 &nbsp;Nodechain &nbsp;| &nbsp;All Rights Reserved</div>
  </footer>
</div>
</body>
</html>
```